Teaching Tool Design

This is a teaching evaluating tool so that teachers can assess how well they are teaching.
Please use the Explicit Instruction Classroom Observation Matrix as the text for the project.
Design a clean, visually aligned version of the Explicit Instruction Observation Matrix that reflects Kestley’s instructional model and LUMA’s framework https://www.learnquarry.edu.au/sites/default/files/2022-08/guided-lesson-rubric-a2.pdf
Use a professional layout with clear column divisions, alternating row shading, and space for observer notes and teacher reflection.
Copy Kestley's style theme https://kestleyshs.qz.edu.au/
Also please see the attached to make a similar style.

```html
<!DOCTYPE html>
<html lang="en">
<head>
<meta charset="utf-8">
<title>Explicit Instruction Rubric – Kestley’s</title>
<link rel="stylesheet" href="https://fonts.googleapis.com/css2?family=Poppins:wght@400;600;700;800&display=swap">
<style>
:root{
  --stage:#4b4b4b;
  --frame:#f1e65a;
  --navy:#1f4394;
  --white:#ffffff;
  --ink:#1d1d1f;
  --teal:#0e848c;
  --teal-tint:#d5e3e7;
  --teal-pale:#eef3f6;
  --magenta:#a91f5a;
  --magenta-tint:#f2dde6;
  --magenta-pale:#f8f1f5;
  --purple:#53318a;
  --purple-tint:#e3e0ed;
  --purple-pale:#f3f1f6;
  --blue:#3566b5;
  --blue-tint:#dfe8f3;
  --blue-pale:#f0f4f9;
}
*{box-sizing:border-box;margin:0;padding:0}
html,body{width:1200px;height:923px;overflow:hidden;background:var(--stage);font-family:"Poppins",sans-serif}
.poster{position:absolute;left:59px;top:90px;width:1073px;height:756px;background:var(--frame)}
.header{position:absolute;left:26px;top:22px;width:1021px;height:61px;background:var(--navy);color:var(--white)}
.brand{position:absolute;left:6px;top:-10px;width:78px;height:90px;display:flex;flex-direction:column;align-items:center;justify-content:center;gap:6px;background:var(--navy);border:2px solid var(--frame);border-radius:6px 6px 39px 39px}
.brand-mark{width:12px;height:12px;background:var(--frame)}
.brand-name{font-weight:700;font-size:13px;color:var(--white)}
.title{position:absolute;left:135px;top:10px;font-weight:800;font-size:35.5px;letter-spacing:-0.2px;line-height:40px}
.instructions{position:absolute;left:710px;top:11px;font-size:12.4px;line-height:13px;font-weight:400}
.rubric{position:absolute;left:26px;top:116px;width:1021px;height:614px;background:var(--white);display:grid;gap:1.5px;
  grid-template-columns:80.5px 103px 81px 89px 73.5px 75px 90.5px 90.5px 80.5px 75px 86.5px 1fr;
  grid-template-rows:97px 110.5px 124.5px 72px 97.5px 53.5px 1fr}
.cell{font-size:8.5px;line-height:9.05px;color:var(--ink);padding:12px 4px 0 5.5px}
.g1{background:var(--teal-pale)} .g1.is-filled{background:var(--teal-tint)}
.g2{background:var(--magenta-pale)} .g2.is-filled{background:var(--magenta-tint)}
.g3{background:var(--purple-pale)} .g3.is-filled{background:var(--purple-tint)}
.g4{background:var(--blue-pale)} .g4.is-filled{background:var(--blue-tint)}
.axis{background:var(--navy);color:var(--white);font-weight:600;display:flex;align-items:center;padding-left:11px;font-size:12px;letter-spacing:-0.3px}
.axis-quality{grid-row:1/6;grid-column:1;align-items:flex-end;padding-bottom:10px;line-height:12.5px;gap:8px}
.axis-quality svg{margin-bottom:2px}
.indicator{color:var(--white);font-size:8.6px;line-height:9.05px;padding:12px 4px 0 5.5px}
.i1{background:var(--teal)} .i2{background:var(--magenta)} .i3{background:var(--purple)} .i4{background:var(--blue)}
.capability{color:var(--white);font-weight:600;font-size:8.1px;line-height:9px;display:flex;align-items:center;gap:10px;padding-left:6px}
.capability .num{flex:none;width:17px;height:17px;border-radius:50%;background:var(--white);font-size:10px;font-weight:400;display:flex;align-items:center;justify-content:center}
.c1{grid-column:2/5;background:var(--teal)} .c1 .num{color:var(--teal)}
.c2{grid-column:5/8;background:var(--magenta)} .c2 .num{color:var(--magenta)}
.c3{grid-column:8/11;background:var(--purple)} .c3 .num{color:var(--purple)}
.c4{grid-column:11/13;background:var(--blue)} .c4 .num{color:var(--blue)}
</style>
</head>
<body>
<div class="poster">
  <header class="header">
    <div class="brand"><span class="brand-mark"></span><span class="brand-name">Kestley’s</span></div>
    <h1 class="title">EXPLICIT INSTRUCTION RUBRIC</h1>
    <p class="instructions">Read the capability and the related criteria.<br>For each capability, identify which criterion<br>best describes your current practice.</p>
  </header>

  <section class="rubric">
    <div class="axis axis-quality"><span>Quality<br>criteria</span>
      <svg width="6" height="34" viewBox="0 0 6 34"><path d="M3 34V2M0.5 5L3 1 5.5 5" stroke="#fff" stroke-width="1" fill="none"/></svg>
    </div>

    <!-- level 4 -->
    <div class="cell g1 is-filled">Anticipates critical points within the learning progression when formatively assessing student learning is most important</div>
    <div class="cell g1"></div>
    <div class="cell g1"></div>
    <div class="cell g2"></div>
    <div class="cell g2"></div>
    <div class="cell g2"></div>
    <div class="cell g3"></div>
    <div class="cell g3 is-filled">Provides additional support that ensures students are optimally challenged in their learning</div>
    <div class="cell g3"></div>
    <div class="cell g4"></div>
    <div class="cell g4 is-filled">Provides immediate feedback that does not reduce cognitive demand</div>

    <!-- level 3 -->
    <div class="cell g1"></div>
    <div class="cell g1 is-filled">Identifies likely challenges and common misconceptions</div>
    <div class="cell g1 is-filled">Sequences chunked tasks based on the learning progression and evidence of what students already know and are able to do</div>
    <div class="cell g2"></div>
    <div class="cell g2"></div>
    <div class="cell g2 is-filled">Refers to learning objectives and success criteria throughout the lesson, particularly when achieved</div>
    <div class="cell g3 is-filled">Sequences multiple worked examples to gradually introduce different elements of the task or alternative ways of completing it</div>
    <div class="cell g3"></div>
    <div class="cell g3 is-filled">Gradually removes scaffolding based on evidence of student learning</div>
    <div class="cell g4 is-filled">Sequences opportunities for independent practice to gradually deepen students' understanding of what they have learned</div>
    <div class="cell g4"></div>

    <!-- level 2 -->
    <div class="cell g1 is-filled">Plans unit based on learning progression</div>
    <div class="cell g1"></div>
    <div class="cell g1 is-filled">Sequences chunked tasks based on the learning progression</div>
    <div class="cell g2 is-filled">Tailors learning objectives from the curriculum for the whole class based on what students already know and are able to do</div>
    <div class="cell g2 is-filled">Sets clear success criteria and stretch goals for the whole class</div>
    <div class="cell g2 is-filled">Develops student understanding of learning objectives and success criteria</div>
    <div class="cell g3"></div>
    <div class="cell g3 is-filled">Provides additional support based on evidence of what students already know and are able to do</div>
    <div class="cell g3"></div>
    <div class="cell g4"></div>
    <div class="cell g4"></div>

    <!-- level 1 -->
    <div class="cell g1 is-filled">Consults the curriculum to identify the common learning progression for the target knowledge and skills</div>
    <div class="cell g1 is-filled">Identifies prerequisite knowledge and skills from the curriculum</div>
    <div class="cell g1 is-filled">Chunks learning into small, manageable tasks</div>
    <div class="cell g2 is-filled">Sets learning objectives from the curriculum for the whole class</div>
    <div class="cell g2 is-filled">Sets clear success criteria for the whole class</div>
    <div class="cell g2 is-filled">Shares learning objectives and success criteria for students</div>
    <div class="cell g3 is-filled">Walks students through all required steps for completing the task using worked examples</div>
    <div class="cell g3 is-filled">Explains knowledge and skills needed to complete the task</div>
    <div class="cell g3 is-filled">Presents some worked examples with removed steps</div>
    <div class="cell g4 is-filled">Provides opportunities for independent practice</div>
    <div class="cell g4 is-filled">Provides immediate feedback to students as they practise</div>

    <!-- level 0 -->
    <div class="cell g1 is-filled">I am yet to include any of these behaviours in my explicit instruction practice</div>
    <div class="cell g1 is-filled">I am yet to include any of these behaviours in my explicit instruction practice</div>
    <div class="cell g1 is-filled">I am yet to include any of these behaviours in my explicit instruction practice</div>
    <div class="cell g2 is-filled">I am yet to include any of these behaviours in my explicit instruction practice</div>
    <div class="cell g2 is-filled">I am yet to include any of these behaviours in my explicit instruction practice</div>
    <div class="cell g2 is-filled">I am yet to include any of these behaviours in my explicit practice instruction</div>
    <div class="cell g3 is-filled">I am yet to include any of these behaviours in my explicit instruction practice</div>
    <div class="cell g3 is-filled">I am yet to include any of these behaviours in my explicit instruction practice</div>
    <div class="cell g3 is-filled">I am yet to include any of these behaviours in my explicit instruction practice</div>
    <div class="cell g4 is-filled">I am yet to include any of these behaviours in my explicit instruction practice</div>
    <div class="cell g4 is-filled" style="padding-top:18px">am yet to include any of these behaviours in my explicit instruction practice</div>

    <!-- indicators -->
    <div class="axis">Indicators</div>
    <div class="indicator i1">Identifies learning progressions from the curriculum</div>
    <div class="indicator i1">Identifies how knowledge and skills build</div>
    <div class="indicator i1">Chunks learning</div>
    <div class="indicator i2">Sets learning objectives</div>
    <div class="indicator i2">Sets success criteria</div>
    <div class="indicator i2">Communicates learning objectives and success criteria</div>
    <div class="indicator i3">Uses worked examples</div>
    <div class="indicator i3">Provides scaffolding when needed</div>
    <div class="indicator i3">Removes scaffolding as needed</div>
    <div class="indicator i4">Provides opportunities for independent practice</div>
    <div class="indicator i4">nteracts with students during practice</div>

    <!-- capabilities -->
    <div class="axis">Capability</div>
    <div class="capability c1"><span class="num">1</span><span>Breaks down complex skills and knowledge into<br>smaller instructional tasks</span></div>
    <div class="capability c2"><span class="num">2</span><span>Sets clear and measurable learning<br>objectives and success criteria</span></div>
    <div class="capability c3"><span class="num">3</span><span>Uses worked examples to demonstrate<br>what students need to learn</span></div>
    <div class="capability c4"><span class="num">4</span><span>Provides opportunities for<br>students to practise what<br>they have learned</span></div>
  </section>
</div>
</body>
</html>
```